Renewable energy company needs modern memorable marketing brochure

We have an 8 page marketing brochure which was created in house. This needs to be revamped and modernised to stand out from our competitors in Australia, Chile and the UK. The brochure should depict us as a professional and dynamic company and instil confidence in prospective clients that we do a professional job. Once the design is finalised we will need a country specific document in the correct language i.e. Spanish for Chile. We are happy to pay for these iterations. We have a company logo which we would like incorporated into the brochure and the colours from the logo utilised where appropriate in the overall design. I have uploaded our existing brochure for an example of the content that the brochure needs to have and can upload the images separately if they are needed. Images in the brochure need to be copyright free and we have lots of photos in-house. I have added all the images from the last brochure and also the text in Indesign so it can be copied easily if needed.

Target Market(s)

landowners and companies

Industry/Entity Type

It Company

Requirements
Must have
• A clean modern look with some colours taken from the logo colour. Be easy to print in various countries.

```html
<!DOCTYPE html>
<html lang="en">
<head>
<meta charset="utf-8">
<title>Solara Fields – Brochure Cover Spread</title>
<link rel="stylesheet" href="https://fonts.googleapis.com/css2?family=Barlow:wght@400;500&family=Arimo:wght@400;700&display=swap">
<style>
  :root {
    --page-bg: #e9e7e3;
    --paper: #ffffff;
    --panel-grey: #a7a8aa;
    --ink: #2b2b2b;
    --ink-soft: #3a3a3a;
    --navy: #2c2f6e;
    --tan: #b39a63;
    --green-dark: #3f6a2a;
    --green-light: #9fb57a;
  }
  * { margin: 0; padding: 0; box-sizing: border-box; }
  html, body { width: 1200px; height: 1200px; overflow: hidden; background: var(--page-bg); }
  .canvas { position: relative; width: 1200px; height: 1200px; }
  .spread {
    position: absolute; left: 40px; top: 205px;
    width: 1320px; height: 932px;
    transform: scale(0.8485); transform-origin: top left;
    background: var(--paper);
    box-shadow: 0 4px 14px rgba(0,0,0,0.25);
    overflow: hidden;
  }
  .shapes { position: absolute; inset: 0; }
  .brand {
    position: absolute; left: 985px; top: 34px;
    display: flex; align-items: center; gap: 26px;
  }
  .brand-dot { width: 96px; height: 96px; border-radius: 50%; background: var(--panel-grey); }
  .brand-name {
    font-family: "Barlow", sans-serif; font-weight: 400;
    font-size: 37px; line-height: 33px; letter-spacing: 1px; color: var(--ink);
  }
  .headline {
    position: absolute; left: 693px; top: 722px;
    font-family: "Barlow", sans-serif; color: var(--ink);
  }
  .headline h1 { font-weight: 500; font-size: 43px; line-height: 48px; letter-spacing: 0.3px; }
  .headline p { font-weight: 500; font-size: 23px; line-height: 29px; margin-top: 4px; color: var(--ink-soft); }
  .contact {
    position: absolute; left: 19px; top: 675px; width: 480px;
    font-family: "Arimo", sans-serif; font-size: 13px; line-height: 16.5px; color: #111;
  }
  .contact .intro { margin-bottom: 30px; }
  .contact .region { font-weight: 700; font-size: 15px; }
  .contact .person { margin-bottom: 14px; }
  .contact .person strong { font-weight: 700; }
  .company {
    position: absolute; right: 679px; top: 837px; width: 260px; text-align: right;
    font-family: "Arimo", sans-serif; font-size: 13px; line-height: 16.3px; color: #111;
  }
  .company strong { font-weight: 700; }
</style>
</head>
<body>
<div class="canvas">
  <section class="spread">
    <svg class="shapes" width="1320" height="932" viewBox="0 0 1320 932">
      <defs>
        <linearGradient id="solar-rows" x1="0" y1="0" x2="1" y2="1">
          <stop offset="0" stop-color="#3a3d7e"/>
          <stop offset="0.55" stop-color="var(--navy)"/>
          <stop offset="1" stop-color="var(--tan)"/>
        </linearGradient>
        <linearGradient id="farm-aerial" x1="0" y1="0" x2="0" y2="1">
          <stop offset="0" stop-color="#b6c08c"/>
          <stop offset="0.3" stop-color="#4a7a3a"/>
          <stop offset="0.45" stop-color="#404a78"/>
          <stop offset="0.55" stop-color="var(--green-dark)"/>
          <stop offset="1" stop-color="#4e7d2c"/>
        </linearGradient>
      </defs>
      <path class="photo-rows" role="img" aria-label="Close aerial photo of long rows of solar panels on dry grass"
            d="M0 0 L595 0 L482 640 Q478 660 456 660 L0 660 Z" fill="url(#solar-rows)"/>
      <path class="panel-grey" d="M660 149 L628 149 Q606 149 601 172 L508 638 Q504 660 527 660 L660 660 Z" fill="var(--panel-grey)"/>
      <path class="photo-farm" role="img" aria-label="Aerial photo of a solar farm between fields and woodland"
            d="M660 149 L1280 149 Q1302 149 1298 172 L1221 639 Q1217 660 1195 660 L660 660 Z" fill="url(#farm-aerial)"/>
      <path class="panel-grey" d="M1320 255 L1320 660 L1258 660 Q1236 660 1241 638 Z" fill="var(--panel-grey)"/>
      <path class="panel-grey" d="M660 677 L1138 677 Q1162 677 1157 700 L1115 932 L660 932 Z" fill="var(--panel-grey)"/>
    </svg>

    <div class="brand">
      <span class="brand-dot"></span>
      <div class="brand-name">SOLARA<br>FIELDS</div>
    </div>

    <div class="headline">
      <h1>INFINITE ENERGY</h1>
      <p>USE YOUR LAND TO HARVEST<br>ENERGY FROM THE SUN</p>
    </div>

    <div class="contact">
      <p class="intro">CONTACT DETAILS<br>If you are interested to learn more about securing a long term income stream<br>from a Solara Fields solar farm on your land please contact us</p>
      <p class="region">Australia</p>
      <p class="person"><strong>Mara Ellison</strong><br>Business Development Associate<br>mara.ellison@solarafields.com.au<br>+61 (0) 400 123 456</p>
      <p class="person"><strong>Tom Reyes</strong><br>Business Development Associate<br>tom.reyes@solarafields.com.au<br>+61 (0) 400 654 321</p>
    </div>

    <div class="company">
      <strong>Solara Fields PTY. Ltd.</strong><br>c/o Harlow Grant &amp; Co, Lower<br>Ground, 48 Ridgeway St, Newstead,<br>Qld, 4000 Australia<br>www.solarafields.com.au
    </div>
  </section>
</div>
</body>
</html>
```